Fundraising Company Needs a Brochure Design

We need a brochure design for a company that helps charities raise money. Our main product is selling art on easels to raise money for various charites. The brochure will have a total of four pages with the size being 8.5" X 11" for each page. All of text will be provided for the brochure. The front page should include our logo and a short intro. The second page will contain a summary along with how the easel program works. The third page will contain information about the companies and charities we work with and other ways we raise money for charities. The back page will contain three testimonials along with our mission/vision statement and our contact information. We also need to include a picture of the easel somewhere in the catalog. The color of our logo is orange and light green but the brochure doesn't need to contain those colors.
The brochure will be presented to major charities and local businesses alike.
It Company

```html
<!DOCTYPE html>
<html lang="en">
<head>
<meta charset="utf-8">
<title>Canvas Commons – Brochure Spread</title>
<link href="https://fonts.googleapis.com/css2?family=PT+Sans:wght@400;700&display=swap" rel="stylesheet">
<style>
  :root {
    --backdrop: #2a2a2a;
    --paper: #ffffff;
    --lime: #cdd72a;
    --lime-light: #dfe55c;
    --lime-dark: #a6b51b;
    --ink: #3b3d17;
    --heading: #24250f;
    --fold: rgba(0, 0, 0, 0.18);
  }
  * { box-sizing: border-box; margin: 0; padding: 0; }
  html, body {
    width: 1200px; height: 793px; overflow: hidden;
    background: var(--backdrop);
    font-family: "PT Sans", Arial, sans-serif;
  }
  .spread {
    position: absolute; left: 28px; top: 26px;
    width: 1144px; height: 740px;
    background: var(--paper);
    overflow: hidden;
  }
  .hero { position: absolute; top: 0; height: 320px; }
  .hero--hands {
    left: 0; width: 572px;
    background: radial-gradient(ellipse at 45% 45%, #f2d6c4 0%, #f6e6dc 35%, #ffffff 75%);
  }
  .hero--people {
    left: 572px; width: 572px;
    background:
      radial-gradient(ellipse 46% 22% at 50% 52%, rgba(176,110,110,.38), rgba(176,110,130,0) 100%),
      radial-gradient(ellipse at 50% 40%, #d6d8dc 0%, #e9eaec 45%, #ffffff 80%);
  }
  .wave { position: absolute; inset: 0; width: 1144px; height: 740px; }
  .fold {
    position: absolute; left: 560px; top: 0; width: 24px; height: 740px;
    background: linear-gradient(90deg, transparent, var(--fold) 50%, transparent);
  }
  .brand {
    position: absolute; top: 24px;
    display: flex; align-items: center; gap: 7px;
    font-weight: 700; font-size: 16px; color: var(--heading);
    text-transform: uppercase; letter-spacing: 1px;
  }
  .brand__dot { width: 12px; height: 12px; border-radius: 50%; background: var(--lime-dark); }
  .brand--left { left: 28px; }
  .brand--right { right: 28px; }
  .column {
    position: absolute; width: 244px;
    color: var(--ink); font-size: 8.1px; line-height: 1.36;
  }
  .column h2 {
    font-size: 11.5px; font-weight: 700; color: var(--heading);
    text-transform: uppercase; line-height: 1.2; margin-bottom: 12px;
  }
  .column h2.section-gap { margin-top: 10px; }
  .column h3 { font-size: 8.3px; font-weight: 700; color: var(--heading); margin-top: 8px; }
  .column p { margin-bottom: 9px; }
  .column ul { list-style: none; margin: 0 0 9px 0; }
  .column li { padding-left: 10px; position: relative; }
  .column li::before { content: "•"; position: absolute; left: 0; }
  .column ul.points li { margin-bottom: 3px; }
  .col-summary { left: 40px; top: 332px; }
  .col-sealed { left: 298px; top: 300px; }
  .col-partners { left: 610px; top: 370px; }
  .col-auctions { left: 868px; top: 332px; }
</style>
</head>
<body>
<main class="spread">
  <div class="hero hero--hands" role="img" aria-label="Photo of many raised hands against a white background"></div>
  <div class="hero hero--people" role="img" aria-label="Photo of a chain of colourful paper cut-out people standing in front of a grey world map"></div>

  <svg class="wave" viewBox="0 0 1144 740" aria-hidden="true">
    <path d="M0,300 C150,298 250,205 400,212 C520,220 570,292 700,328 C830,362 1000,300 1144,245 L1144,740 L0,740 Z" fill="var(--lime-light)"/>
    <path d="M0,318 C160,316 260,228 405,236 C525,244 575,310 705,344 C835,376 1005,318 1144,266 L1144,740 L0,740 Z" fill="var(--lime)"/>
    <path d="M0,722 C260,712 620,736 1144,716 L1144,740 L0,740 Z" fill="var(--lime-dark)"/>
  </svg>
  <div class="fold"></div>

  <div class="brand brand--left"><span class="brand__dot"></span>Canvas Commons</div>
  <div class="brand brand--right"><span class="brand__dot"></span>Canvas Commons</div>

  <section class="column col-summary">
    <h2>Summary</h2>
    <p>Canvas Commons was created as a new way for communities to work together and collectively raise money for deserving charities. We help charitable organizations, local establishments, and citizens to work hand in hand, to help those in need. At Canvas Commons, we bring charity, business, and people together to help raise money through Sealed Bid Auctions.</p>
    <ul class="points">
      <li>Establishments host a rotating collection of art, appropriately selected for their type of organization or business.</li>
      <li>Generous customers submit bids, on location, for the art, with the highest bidder claiming the piece of art.</li>
      <li>The establishment gets increased traffic and helps a charity of their choice.</li>
      <li>The charity selected by the establishment receives a portion of the profits from the auction.</li>
    </ul>
    <p>A Sealed Bid Auction, organized by Canvas Commons, is an ideal way for businesses and other establishments to fundraise for a charity of their choice. There are no costs for the hosts associated with the auction and all auction materials are supplied by Canvas Commons. We handle all the details, manage the auction, handle the presentation and delivery of the art, and oversee the completion of the purchases. The only cost to the host establishment is four square feet of floor space.</p>
    <p>Canvas Commons has raised thousands of dollars for many different charities, both large and small, for special projects or long-term initiatives. The simplicity of this program is what makes it successful, but bringing a community together to help those in need makes everyone a winner.</p>
  </section>

  <section class="column col-sealed">
    <h2>Sealed Bid Auctions and How They Work</h2>
    <p>Sealed Bid Auctions, organized by Canvas Commons, are effortless but rewarding ways for local establishments and organizations to raise money for charities of their choice.</p>
    <p>It's easier than you think. In a host's space, a piece of art is put up for auction. Customers interested in owning the art submit bid amounts on pieces of paper on location by sealing their bid in an envelope and placing it in a box. There will be a minimum bid for each item in an auction. This will be the original cost for the item up for bid plus additional costs incurred in the process of readying it for auction. The highest bid wins the auction and the item is sold. Profit from the auction goes to a charity preselected by the location hosting the auction.</p>
    <p>The auctions are an easy and straightforward process for both the hosts and the charities. Canvas Commons takes care of all the details. We supply the artwork and a smart easel on which to display it. We provide the signage and Sealed Bid Auction materials, contact the winner, and manage the purchase and delivery details. Any other associated effort or costs are also our responsibility.</p>
    <p>The four square feet of floor space, donated by the host establishment, will host a new piece of art every three weeks. Each piece of art is selected with the charity or the host establishment in mind. They are typically limited edition oil paintings or prints including works by the Northern Ten, selected photography, as well as sport and music inspired art. An employee from Canvas Commons handles the replacement of each piece of art, and readies the space for the next three weeks of sealed bidding.</p>
    <p>The original cost of the artwork, and other associated costs generate the minimum bid, while every cent surpassing the minimum goes directly to the chosen charity.</p>
  </section>

  <section class="column col-partners">
    <h2>Who We Work With</h2>
    <p>Canvas Commons has raised money for a broad range of charities and causes. While we work with everyone, no specific group or category of charity is favoured to receive donations from our Sealed Bid Auctions.</p>
    <p>The charities chosen by the host establishment are commonly selected for the benefits and assistance that charity can bring to the community. Community is the heart of Canvas Commons, helping local establishments and their patrons or members work together to improve their communities.</p>
    <p>Similarly, the establishments that host Sealed Bid auctions with Canvas Commons run the gamut. We have partnered with and held Sealed Bid Auctions at:</p>
    <ul>
      <li>Hospitals</li>
      <li>Retailers</li>
      <li>Galleries</li>
      <li>Restaurants</li>
      <li>Concerts</li>
      <li>Public Events</li>
      <li>Hotels</li>
      <li>Sporting Events/Arenas</li>
    </ul>
    <p>Businesses and other locations having hosted our Sealed Bid Auctions view them as more than simply a valuable way to help raise funds for charity. They've viewed their partnership with Canvas Commons as a valuable way to help themselves and improve the health of their community.</p>
  </section>

  <section class="column col-auctions">
    <p>The Sealed Bid Auctions actually attract visitors and customers to establishments. With the classy presentation of the art as provided by Canvas Commons, it is like having a small museum for patrons. With the art always being exceptional, word of mouth travels fast.</p>
    <p>The positive effects to a company's reputation can be tremendous. It is no secret people favour businesses that add to the betterment of their community.</p>
    <h2 class="section-gap">Silent/Live Auctions</h2>
    <p>The Sealed Bid Auction isn't the only way Canvas Commons helps raise money for charities. We are also very experienced at running Silent and Live Auctions.</p>
    <h3>Silent Auctions</h3>
    <p>Canvas Commons does it all for you. We supply some or all of the products for your fundraising event, offering products ranging in value from $100 up to $10,000. We even supply the bid sheets and cashiers, all at no cost outlay to you or your charity. All monies bid over the fair starting bid is passed onto your organization.</p>
    <h3>Live Auctions</h3>
    <p>Daniel Corwin has years of fulltime experience in the auction business and has performed hundreds of fundraising auctions. His humour and style has the gift of getting the most money and support from audiences.</p>
    <p>Like our Sealed Bid Auctions, a Silent or Live Auction comes with all of the collateral and signage, auction tools or auctioneer, and the artwork necessary to have a successful auction. We will do all of the work and cover all of the costs. These costs are recovered in the sale of the items up for bid, with all profit going directly to charity.</p>
  </section>
</main>
</body>
</html>
```